Pelvane Tonic Social Media Graphics

Focusing on the Pelvane Tonic product, create 6-7 individual social media graphics (square size). For the color scheme of the graphics, they should all be complementary with the Pelvane Tonic bottle colors.

Note: each graphic should have one of the 3 pictures of the bottle on it and/or one of the images with a person on it (several pics attached)/only use stock photography that I provided.

Target Market(s)

men and women who need to lose weight

Industry/Entity Type

health and wellness

Colors
A7469A
B969AE
D3A5CF
EDDBEB
F8F0F9

Requirements
Must have
• product pictures
Nice to have
• stock photography that is included

```html
<!DOCTYPE html>
<html lang="en">
<head>
<meta charset="utf-8">
<title>Pelvane Tonic Social Media Graphics</title>
<link rel="stylesheet" href="https://fonts.googleapis.com/css2?family=Archivo+Black&family=Ubuntu:wght@400;500;700&display=swap">
<style>
:root{
  --stage:#4e2655;
  --plum-deep:#3d1044;
  --plum:#6a1f6e;
  --magenta:#a7469a;
  --orchid:#b969ae;
  --lilac:#d3a5cf;
  --blush:#eddbeb;
  --mist:#f8f0f9;
  --white:#ffffff;
  --ink:#2a1a2c;
}
*{margin:0;padding:0;box-sizing:border-box}
html,body{width:1200px;height:1200px;overflow:hidden;background:var(--stage)}
body{position:relative;font-family:"Ubuntu",sans-serif}
.post{position:absolute;width:320px;height:320px;overflow:hidden;box-shadow:0 8px 22px rgba(20,0,25,.35)}
.post > *{position:absolute}
.bg{left:0;top:0;width:320px;height:320px}
.post-1{left:81px;top:208px;background:var(--white)}
.post-2{left:450px;top:208px;background:var(--white)}
.post-3{left:811px;top:208px;background:linear-gradient(90deg,var(--plum-deep),#7c2b80)}
.post-4{left:81px;top:586px;background:var(--plum-deep)}
.post-5{left:453px;top:586px;background:linear-gradient(180deg,var(--white) 55%,var(--blush))}
.post-6{left:815px;top:588px;background:var(--white)}
.brand{left:33px;top:20px;display:flex;align-items:center;gap:3px;font-weight:700;font-size:8px;letter-spacing:-.1px;z-index:2}
.brand .ring{width:22px;height:22px;border:1px solid currentColor;border-radius:50%;opacity:.6}
.brand.light{color:var(--white)}
.brand.pink{color:var(--magenta)}
.brand.soft{color:var(--orchid)}
.photo{border-radius:4px}
.bottle{border-radius:8px 8px 5px 5px;background:linear-gradient(180deg,#fff 0%,#f3eef4 60%,var(--lilac) 100%);box-shadow:0 2px 5px rgba(0,0,0,.2)}
.headline{font-family:"Archivo Black",sans-serif;line-height:.98;text-transform:uppercase;z-index:2}
.copy{z-index:2}
.footer{display:flex;align-items:center;gap:9px;font-size:5.5px;z-index:2}
.footer .dot{width:6px;height:6px;border-radius:50%;border:1px solid currentColor}
.footer .url{margin-left:3px}
.footer.dark{color:var(--ink)}
.footer.pink{color:var(--orchid)}
.benefits{list-style:none;font-size:8.6px;color:var(--ink);line-height:14px}
.benefits li{display:flex;align-items:center;gap:8px}
.benefits li::before{content:"";width:4px;height:4px;background:var(--magenta)}
</style>
</head>
<body>

<section class="post post-1">
  <svg class="bg" viewBox="0 0 320 320">
    <defs><linearGradient id="p1g" x1="0" y1="0" x2="1" y2="1"><stop offset="0" stop-color="#8e3590"/><stop offset="1" stop-color="#a7469a"/></linearGradient></defs>
    <path d="M0 0H320V165C270 150 230 160 170 168C110 176 50 180 0 183Z" fill="url(#p1g)"/>
    <g fill="none" stroke="#5a1a5e" stroke-width="4" opacity=".6"><circle cx="300" cy="30" r="60"/><circle cx="300" cy="30" r="75"/></g>
    <path d="M320 215C260 220 218 260 218 320H320Z" fill="#6a1f6e"/>
    <path d="M320 272C295 272 275 292 275 320H320Z" fill="#fff"/>
  </svg>
  <div class="brand light"><span>Pelvane Tonic</span><span class="ring"></span></div>
  <div class="photo" role="img" aria-label="Woman in white sportswear measuring her waist with a tape" style="left:150px;top:0;width:155px;height:170px;background:linear-gradient(180deg,#c89a80,#8a5b4c)"></div>
  <h2 class="headline" style="left:33px;top:84px;font-size:26.5px;color:var(--white)">Burn<br>Fat<br>Faster</h2>
  <ul class="benefits" style="left:34px;top:203px">
    <li>Melt away stubborn fat, especially belly &amp; back fat</li>
    <li>Accelerate overall weight loss</li>
    <li>Boost energy and mental clarity</li>
    <li>Get whiter eyes and glowing skin</li>
  </ul>
  <div class="bottle" role="img" aria-label="Pelvane Tonic bottle" style="left:257px;top:190px;width:42px;height:73px"></div>
  <div class="footer dark" style="left:34px;top:286px"><span class="dot"></span><span class="dot"></span><span class="dot"></span><span class="url">www.pelvanetonic.com</span></div>
</section>

<section class="post post-2">
  <svg class="bg" viewBox="0 0 320 320">
    <g fill="none" stroke="#a7469a" stroke-width="3" opacity=".8"><circle cx="285" cy="40" r="55"/><circle cx="285" cy="40" r="65"/></g>
    <path d="M0 300C60 285 120 300 190 290C250 280 290 280 320 295V320H0Z" fill="#a7469a"/>
  </svg>
  <div class="brand pink" style="left:39px"><span>Pelvane Tonic</span><span class="ring"></span></div>
  <div class="photo" role="img" aria-label="Woman in black sportswear measuring her waist with a tape" style="left:118px;top:0;width:190px;height:171px;background:linear-gradient(180deg,#9a6b55,#3a2a2a)"></div>
  <p class="copy" style="left:37px;top:73px;font-size:15px;font-weight:500;line-height:20px;color:var(--magenta)">Struggling<br>to Lose<br>Weight?</p>
  <div style="left:27px;top:171px;width:265px;height:92px;border-radius:9px;background:linear-gradient(90deg,var(--plum-deep),var(--magenta))"></div>
  <p class="copy" style="left:46px;top:183px;font-size:12px;color:var(--orchid)">Try This</p>
  <h2 class="headline" style="left:45px;top:199px;font-size:23px;color:var(--white)">Fat Flush<br>Secret</h2>
  <div class="bottle" role="img" aria-label="Three Pelvane Tonic bottles" style="left:191px;top:218px;width:84px;height:56px;border-radius:6px"></div>
  <div class="footer dark" style="left:40px;top:286px"><span class="dot"></span><span class="dot"></span><span class="dot"></span><span class="url">www.pelvanetonic.com</span></div>
</section>

<section class="post post-3">
  <svg class="bg" viewBox="0 0 320 320">
    <g fill="none" stroke="#b969ae" stroke-width="3" opacity=".55"><circle cx="300" cy="60" r="75"/><circle cx="300" cy="60" r="88"/><circle cx="300" cy="60" r="100"/></g>
  </svg>
  <div class="brand soft" style="left:48px"><span>Pelvane Tonic</span><span class="ring"></span></div>
  <div class="photo" role="img" aria-label="Smiling woman in sportswear holding a bathroom scale and an apple" style="left:160px;top:85px;width:125px;height:235px;background:linear-gradient(180deg,#8c5a48,#2e2230)"></div>
  <div class="bottle" role="img" aria-label="Three Pelvane Tonic bottles" style="left:228px;top:58px;width:54px;height:36px;border-radius:5px"></div>
  <p class="copy" style="left:38px;top:80px;font-size:19px;font-weight:500;color:var(--white)">Accelerate</p>
  <h2 class="headline" style="left:38px;top:106px;font-size:27px;line-height:1.05;color:var(--white)">Your<br>Weight<br>Loss</h2>
  <p class="copy" style="left:38px;top:208px;font-size:10.5px;color:var(--orchid)">With This Easy Fat Flush</p>
  <div class="footer pink" style="left:38px;top:279px"><span class="dot"></span><span class="dot"></span><span class="dot"></span><span class="url">www.pelvanetonic.com</span></div>
</section>

<section class="post post-4">
  <svg class="bg" viewBox="0 0 320 320">
    <g fill="none" stroke="#1f0625" stroke-width="4" opacity=".8"><circle cx="210" cy="25" r="50"/><circle cx="210" cy="25" r="64"/><circle cx="210" cy="25" r="78"/></g>
  </svg>
  <div class="brand soft" style="left:48px"><span>Pelvane Tonic</span><span class="ring"></span></div>
  <div style="left:44px;top:57px;width:229px;height:175px;border-radius:12px;background:linear-gradient(180deg,var(--magenta),var(--plum-deep))"></div>
  <span class="copy" style="left:162px;top:78px;font-size:46px;font-style:italic;color:var(--orchid);opacity:.9">&amp;</span>
  <h2 class="headline" style="left:65px;top:92px;font-size:29px;color:var(--white)">Detox</h2>
  <h2 class="headline" style="left:64px;top:125px;font-size:38px;line-height:1.1;color:var(--white)">Burn<br>Fat</h2>
  <div class="bottle" role="img" aria-label="Pelvane Tonic bottle" style="left:187px;top:156px;width:61px;height:110px"></div>
  <p class="copy" style="left:65px;top:228px;font-size:9.5px;line-height:12px;color:var(--orchid)">The 1-Step Solution<br>for a Slimmer You</p>
  <div class="footer pink" style="left:66px;top:285px"><span class="dot"></span><span class="dot"></span><span class="dot"></span><span class="url">www.pelvanetonic.com</span></div>
</section>

<section class="post post-5">
  <svg class="bg" viewBox="0 0 320 320">
    <g fill="none" stroke="#d3a5cf" stroke-width="4" opacity=".8"><circle cx="270" cy="55" r="70"/><circle cx="270" cy="55" r="84"/></g>
    <path d="M320 215C250 218 212 262 212 320H320Z" fill="#8e3590"/>
    <path d="M320 275C292 275 275 295 275 320H320Z" fill="#fff"/>
  </svg>
  <div class="brand pink" style="left:54px"><span>Pelvane Tonic</span><span class="ring"></span></div>
  <div style="left:36px;top:62px;width:228px;height:162px;border-radius:12px;background:linear-gradient(90deg,var(--magenta),var(--plum-deep))"></div>
  <div class="photo" role="img" aria-label="Cheerful woman in sports top holding a bathroom scale and flexing" style="left:185px;top:125px;width:125px;height:195px;background:linear-gradient(180deg,#a0705a,#3a2a30)"></div>
  <p class="copy" style="left:53px;top:83px;font-size:12px;line-height:16px;color:var(--white)">Flush Away 5-10 Pounds<br>of Toxic Fat</p>
  <h2 class="headline" style="left:53px;top:118px;font-size:29px;color:var(--white)">In Just<br>Weeks!</h2>
  <div class="footer pink" style="left:46px;top:281px"><span class="dot"></span><span class="dot"></span><span class="dot"></span><span class="url">www.pelvanetonic.com</span></div>
</section>

<section class="post post-6">
  <svg class="bg" viewBox="0 0 320 320">
    <g fill="none" stroke="#eddbeb" stroke-width="4"><circle cx="270" cy="20" r="70"/><circle cx="270" cy="20" r="85"/><circle cx="270" cy="20" r="100"/></g>
    <path d="M320 198C250 200 200 250 200 320H320Z" fill="#8e3590"/>
    <path d="M320 265C290 265 268 290 268 320H320Z" fill="#fff"/>
  </svg>
  <div class="brand pink" style="left:39px"><span>Pelvane Tonic</span><span class="ring"></span></div>
  <p class="copy" style="left:38px;top:72px;font-size:16.5px;font-weight:500;color:var(--magenta)">The Hidden Key to</p>
  <h2 class="headline" style="left:38px;top:99px;font-size:37px;line-height:1.12;color:var(--magenta)">Weight<br>Loss</h2>
  <p class="copy" style="left:38px;top:219px;font-size:14.5px;font-weight:500;color:var(--magenta)">#Liver Health</p>
  <div class="bottle" role="img" aria-label="Pelvane Tonic bottle" style="left:232px;top:148px;width:61px;height:112px"></div>
  <div class="footer" style="left:39px;top:283px;color:var(--magenta)"><span class="dot"></span><span class="dot"></span><span class="dot"></span><span class="url">www.pelvanetonic.com</span></div>
</section>

</body>
</html>
```